Complete redesign of Licensed Medical Cannabis Dispensary website

Redesign website to modernize it and simplify it and add a self service reservation/preorder interactive delivery form. Also integrate current POS system that has current inventory. Here is a website for inspiration that I really like because of it simplicity https://www.grovaleaf.example and easy ordering option. Attached is our logo.... please design around that and this is our website address www.mistrelcourierhouse.example

Font styles to use
Sans Serif

Colors
5c5c5c
cbcbcb
000000
add136

Requirements
Must have
• inventory thats integrated with pos
• online reservation/delivery form
Nice to have
• a website thats modern and simple
• The website designed are the logo that is attached
Should not have
• too much information

```html
<!DOCTYPE html>
<html lang="en">
<head>
<meta charset="utf-8">
<title>Mistrel Courier — Medical Delivery</title>
<link rel="stylesheet" href="https://fonts.googleapis.com/css2?family=Montserrat:wght@400;500;600;700;800&display=swap">
<style>
:root{
  --green:#add136;
  --green-dark:#8fb21f;
  --ink:#000000;
  --grey:#5c5c5c;
  --light:#cbcbcb;
  --hero-bg:#f2f0f0;
  --band:#4a4a4a;
  --white:#ffffff;
}
*{box-sizing:border-box;margin:0;padding:0}
html,body{width:1200px;height:3371px;overflow:hidden}
body{position:relative;font-family:'Montserrat',sans-serif;color:var(--ink);background:var(--white)}
.abs{position:absolute}

/* header + hero */
.hero{position:absolute;left:0;top:0;width:1200px;height:663px;background:var(--hero-bg);overflow:hidden}
.brand{position:absolute;display:flex;align-items:center;gap:14px;font-weight:700;color:var(--green-dark);font-size:26px}
.brand-dot{width:60px;height:60px;border-radius:50%;background:var(--green-dark)}
.orders{left:692px;top:26px;display:flex;gap:10px;align-items:center}
.orders small{display:block;font-size:11px;font-weight:600}
.orders b{display:block;font-size:15px;color:var(--green-dark)}
.auth{left:858px;top:27px;display:flex}
.auth span{border:1px solid var(--light);background:var(--white);font-size:9px;font-weight:600;padding:6px 8px}
.cart{left:984px;top:26px;display:flex;gap:8px;align-items:center;font-size:10px;font-weight:600}
.cart em{font-style:normal;color:var(--green-dark);display:block}
.cart-box{width:24px;height:26px;background:var(--ink);border-radius:3px;color:var(--green);font-size:10px;display:flex;align-items:center;justify-content:center}
.nav{top:79px;left:643px;display:flex;align-items:center;font-size:11px;font-weight:600}
.nav a{color:var(--ink);text-decoration:none;margin-right:36px}
.nav a.active{background:var(--green);color:var(--white);padding:5px 11px;border-radius:4px;margin-right:32px}
.nav a:last-child{margin-right:0}
.hero-media{left:500px;top:150px;width:600px;height:480px;border-radius:50%;background:radial-gradient(ellipse at 55% 50%,#c9d0b2 0%,#9aa473 35%,#707b45 58%,rgba(242,240,240,0) 72%)}
.hero-text{z-index:2}
.hero-title{left:153px;top:222px;font-size:48px;line-height:56px;font-weight:800;color:var(--green);white-space:nowrap}
.hero-sub{left:153px;top:338px;font-size:30px;font-weight:500;white-space:nowrap}
.hero-copy{left:157px;top:398px;font-size:13px;line-height:21px;width:300px}
.btn{display:inline-flex;align-items:center;justify-content:center;background:var(--green);color:var(--white);font-weight:700;text-decoration:none}
.shop-now{left:157px;top:470px;width:153px;height:45px;border-radius:8px;font-size:17px}
.arrow{top:337px;width:40px;height:38px;background:var(--grey);display:flex;align-items:center;justify-content:center;z-index:3}

/* steps */
.step{position:absolute;width:260px;text-align:center}
.step h3{font-size:14px;font-weight:700}
.step p{margin-top:10px;font-size:11px;line-height:15px;color:var(--ink);padding:0 20px}
.rule{left:0;top:1081px;width:1200px;height:1px;background:#e6e6e6}

/* products */
.section-title{left:0;top:1160px;width:1200px;text-align:center;font-size:22px;font-weight:700}
.filters{left:434px;top:1249px;display:flex;gap:11px}
.filters span{height:32px;display:flex;align-items:center;padding:0 16px;border-radius:4px;background:var(--light);color:var(--white);font-size:11px;font-weight:700}
.filters span.on{background:var(--green);padding:0 25px}
.card{position:absolute;width:215px;height:333px;background:var(--white);box-shadow:0 2px 14px rgba(0,0,0,.12);text-align:center}
.card .shot{width:170px;height:160px;margin:32px auto 0;border-radius:50%}
.card h4{margin-top:30px;font-size:14px;font-weight:600}
.card .price{margin-top:4px;font-size:19px;font-weight:700;color:var(--green-dark)}
.card .buy{display:inline-flex;margin-top:8px;width:90px;height:28px;background:var(--grey);color:var(--white);font-size:10px;font-weight:700;align-items:center;justify-content:center}
.flower{background:radial-gradient(circle,#6b7a35 0%,#8d9a55 45%,rgba(255,255,255,0) 70%)}
.cartridge{background:linear-gradient(90deg,rgba(255,255,255,0) 40%,#2a2a2a 44%,#5a4a1a 52%,#2a2a2a 58%,rgba(255,255,255,0) 62%);border-radius:6px}
.soil{background:radial-gradient(ellipse,#7a5436 0%,#a27a5a 45%,rgba(255,255,255,0) 70%)}
.wax{background:radial-gradient(ellipse,#e8e2c4 0%,#d9cf9e 45%,rgba(255,255,255,0) 70%)}
.oil{background:radial-gradient(circle,#d49a2a 0%,#e3b868 40%,#efe0cf 60%,rgba(255,255,255,0) 72%)}
.tincture{background:linear-gradient(180deg,#f2f2f2,#e2e2e2);border-radius:0}
.tincture::after{content:"";display:block;width:60px;height:110px;margin:30px auto 0;background:linear-gradient(#3a2a1a,#8a4a1a);border-radius:8px}
.jar{background:radial-gradient(ellipse,#e58a2a 0%,#9aa164 45%,rgba(255,255,255,0) 70%)}
.view-more{left:494px;top:2496px;width:214px;height:39px;font-size:13px}

/* band */
.band{left:0;top:2629px;width:1200px;height:332px;background:var(--band);color:var(--white)}
.band-divider{left:600px;top:0;width:1px;height:332px;background:#666}
.band h2{position:absolute;width:600px;text-align:center;font-size:26px;font-weight:400;line-height:36px}
.band h2 b{font-weight:700}
.online-price{left:209px;top:157px;width:285px;height:41px;background:#c9c9c9;color:var(--grey);font-size:22px;font-weight:500;display:flex;align-items:center;justify-content:center}
.online-price s{font-weight:700;margin-left:6px}
.band .btn{height:39px;font-size:12px}

/* footer */
.f-head{font-size:12px;font-weight:700}
.field{position:absolute;height:29px;border:1px solid #9a9a9a;font-size:10px;padding:0 8px;display:flex;align-items:center;justify-content:space-between}
.f-list{list-style:none;font-size:11px;line-height:19.5px}
.social{display:flex;align-items:center;gap:10px;font-size:11px;height:26px;margin-bottom:13px}
.social i{width:26px;height:26px;border-radius:50%;background:#1d3b70}
.f-rule{left:575px;top:3209px;width:492px;height:1px;background:#ddd}
.copy{left:872px;top:3284px;font-size:11px}
</style>
</head>
<body>

<header class="hero">
  <div class="brand" style="left:130px;top:34px"><span class="brand-dot"></span>Mistrel Courier</div>
  <div class="abs orders">
    <svg width="20" height="20" viewBox="0 0 24 24"><path d="M6.6 10.8a15 15 0 0 0 6.6 6.6l2.2-2.2c.3-.3.7-.4 1-.2 1.1.4 2.3.6 3.6.6.6 0 1 .4 1 1V20c0 .6-.4 1-1 1A17 17 0 0 1 3 4c0-.6.4-1 1-1h3.5c.6 0 1 .4 1 1 0 1.3.2 2.5.6 3.6.1.3 0 .7-.2 1z" fill="#000"/></svg>
    <div><small>Orders :</small><b>555-014-2290</b></div>
  </div>
  <div class="abs auth"><span>LOGIN</span><span>SIGNUP</span></div>
  <div class="abs cart"><div>MY CART<em>$0.00</em></div><div class="cart-box">0</div></div>
  <nav class="abs nav">
    <a class="active" href="#">HOME</a><a href="#">ABOUT</a><a href="#">PRODUCTS</a><a href="#">SERVICES</a><a href="#">CONTACT</a>
  </nav>

  <div class="abs hero-media" role="img" aria-label="Glass jar of cannabis flower tipped over with buds spilling out"></div>
  <h1 class="abs hero-title hero-text">TOP SHELF<br>MEDICAL</h1>
  <p class="abs hero-sub hero-text">Marijuana Delivery</p>
  <p class="abs hero-copy hero-text">We offer only the highest quality flowers, edibles and concentrates.</p>
  <a class="abs btn shop-now hero-text" href="#">SHOP NOW</a>

  <div class="abs arrow" style="left:0"><svg width="12" height="14" viewBox="0 0 12 14"><path d="M9 1 3 7l6 6" stroke="#fff" stroke-width="3" fill="none"/></svg></div>
  <div class="abs arrow" style="left:1160px"><svg width="12" height="14" viewBox="0 0 12 14"><path d="m3 1 6 6-6 6" stroke="#fff" stroke-width="3" fill="none"/></svg></div>
</header>

<section>
  <svg class="abs" style="left:0;top:726px" width="1200" height="160" viewBox="0 0 1200 160">
    <g fill="none" stroke="#555" stroke-width="2" stroke-dasharray="5 5">
      <path d="M345 60 Q420 40 495 90"/><path d="M690 130 Q780 130 845 80"/>
    </g>
    <path d="m488 82 10 10-14 2z" fill="#555"/><path d="m838 74 12 2-6 11z" fill="#555"/>
    <g fill="#add136">
      <circle cx="254" cy="76" r="76"/><circle cx="600" cy="76" r="76"/><circle cx="946" cy="76" r="76"/>
    </g>
    <g fill="#fff"><circle cx="254" cy="76" r="57"/><circle cx="600" cy="76" r="57"/><circle cx="946" cy="76" r="57"/></g>
    <g fill="#add136">
      <path d="M236 50h26l10 10v38h-36z"/>
      <circle cx="264" cy="86" r="10" fill="#fff" stroke="#add136" stroke-width="3"/>
      <path d="m259 86 4 4 6-7" stroke="#add136" stroke-width="2.5" fill="none"/>
      <path d="M574 56h8l6 28h26l6-20h-34" stroke="#add136" stroke-width="5" fill="none"/>
      <circle cx="592" cy="96" r="5"/><circle cx="612" cy="96" r="5"/>
      <rect x="928" y="62" width="36" height="30" rx="3"/>
      <path d="M928 74h36" stroke="#fff" stroke-width="3"/>
    </g>
  </svg>
  <div class="step" style="left:124px;top:930px"><h3>GET VERIFIED</h3><p>It's fast. It's simple. Just fill out our verification form and get approved in minutes</p></div>
  <div class="step" style="left:470px;top:930px"><h3>SHOP</h3><p>Add the products you want to your shopping cart and check out. No credit card required!</p></div>
  <div class="step" style="left:816px;top:930px"><h3>GET MEDICATED</h3><p>Sit back and wait. Our professional staff will deliver your medication right to your front door.</p></div>
  <div class="abs rule"></div>
</section>

<section>
  <h2 class="abs section-title">PRODUCTS</h2>
  <div class="abs filters"><span class="on">ALL</span><span>FLOWERS</span><span>CONCENTRATE</span></div>

  <article class="card" style="left:133px;top:1366px"><div class="shot flower" role="img" aria-label="Cannabis flower buds"></div><h4>Valley Haze</h4><p class="price">$ 35.00</p><span class="buy">BUY NOW</span></article>
  <article class="card" style="left:371px;top:1366px"><div class="shot flower" role="img" aria-label="Cannabis flower buds"></div><h4>Valley Haze</h4><p class="price">$ 35.00</p><span class="buy">BUY NOW</span></article>
  <article class="card" style="left:611px;top:1366px"><div class="shot flower" role="img" aria-label="Cannabis flower buds"></div><h4>Valley Haze</h4><p class="price">$ 35.00</p><span class="buy">BUY NOW</span></article>
  <article class="card" style="left:852px;top:1366px"><div class="shot cartridge" role="img" aria-label="Vape oil cartridge"></div><h4>Berrylite Cart.</h4><p class="price">$ 35.00</p><span class="buy">BUY NOW</span></article>

  <article class="card" style="left:133px;top:1726px"><div class="shot soil" role="img" aria-label="Ground hash pile"></div><h4>Valley Haze</h4><p class="price">$ 35.00</p><span class="buy">BUY NOW</span></article>
  <article class="card" style="left:371px;top:1726px"><div class="shot wax" role="img" aria-label="Pale wax concentrate"></div><h4>Valley Haze</h4><p class="price">$ 35.00</p><span class="buy">BUY NOW</span></article>
  <article class="card" style="left:611px;top:1726px"><div class="shot oil" role="img" aria-label="Amber oil concentrate on a dish"></div><h4>Valley Haze</h4><p class="price">$ 35.00</p><span class="buy">BUY NOW</span></article>
  <article class="card" style="left:852px;top:1726px"><div class="shot flower" role="img" aria-label="Cannabis flower bud"></div><h4>Berrylite Cart.</h4><p class="price">$ 35.00</p><span class="buy">BUY NOW</span></article>

  <article class="card" style="left:133px;top:2085px"><div class="shot tincture" role="img" aria-label="Tincture dropper bottle with buds"></div><h4>Valley Haze</h4><p class="price">$ 35.00</p><span class="buy">BUY NOW</span></article>
  <article class="card" style="left:371px;top:2085px"><div class="shot jar" role="img" aria-label="Pill bottle with cannabis buds"></div><h4>Valley Haze</h4><p class="price">$ 35.00</p><span class="buy">BUY NOW</span></article>
  <article class="card" style="left:611px;top:2085px"><div class="shot flower" role="img" aria-label="Single cannabis bud"></div><h4>Valley Haze</h4><p class="price">$ 35.00</p><span class="buy">BUY NOW</span></article>
  <article class="card" style="left:852px;top:2085px"><div class="shot flower" role="img" aria-label="Cannabis flower buds"></div><h4>Berrylite Cart.</h4><p class="price">$ 35.00</p><span class="buy">BUY NOW</span></article>

  <a class="abs btn view-more" href="#">VIEW MORE PRODUCTS</a>
</section>

<section class="abs band">
  <div class="abs band-divider"></div>
  <h2 style="left:0;top:68px">Don’t have <b>your doctor’s</b><br>recommendation yet?</h2>
  <div class="abs online-price">Get it online for just <s>$49!</s></div>
  <a class="abs btn" style="left:272px;top:222px;width:146px" href="#">GET STARTED</a>
  <h2 style="left:600px;top:68px">Still not a <b>member</b><br>of our dispensary?</h2>
  <a class="abs btn" style="left:735px;top:168px;width:191px" href="#">GET VERIFIED NOW</a>
</section>

<footer>
  <h4 class="abs f-head" style="left:133px;top:3022px">ONLINE RESERVATION</h4>
  <div class="field" style="left:133px;top:3056px;width:195px">Name</div>
  <div class="field" style="left:335px;top:3056px;width:195px">E mail</div>
  <div class="field" style="left:133px;top:3094px;width:195px">DATE (dd/mm/yyyy)
    <svg width="12" height="12" viewBox="0 0 12 12"><rect x="1" y="2" width="10" height="9" fill="none" stroke="#000"/><path d="M1 5h10" stroke="#000"/></svg></div>
  <div class="field" style="left:335px;top:3094px;width:195px">Phone</div>
  <div class="field" style="left:133px;top:3137px;width:397px;height:117px;align-items:flex-start;padding-top:6px">Message</div>
  <a class="abs btn" style="left:133px;top:3276px;width:103px;height:38px;font-size:13px" href="#">SUBMIT</a>

  <h4 class="abs f-head" style="left:575px;top:3022px">LINKS</h4>
  <ul class="abs f-list" style="left:575px;top:3054px"><li>Store</li><li>Cart</li><li>My Account</li><li>New Patient Verification</li><li>Contact Us</li></ul>
  <h4 class="abs f-head" style="left:746px;top:3022px">FORUMS</h4>
  <ul class="abs f-list" style="left:746px;top:3054px"><li>Bongs, Bubblers, &amp; Water Pipes</li><li>Concentrates</li><li>Growing</li><li>Vaporizers</li><li>What Are You Smokin'?</li></ul>
  <h4 class="abs f-head" style="left:957px;top:3022px">FOLLOW US ON</h4>
  <div class="abs" style="left:957px;top:3054px">
    <div class="social"><i></i>Friendsy</div>
    <div class="social"><i style="background:#2a8bd0"></i>Chirper</div>
    <div class="social"><i style="background:#0d2f5a"></i>Linkwork</div>
  </div>
  <div class="abs f-rule"></div>
  <div class="brand" style="left:584px;top:3252px;font-size:20px"><span class="brand-dot" style="width:48px;height:48px"></span>Mistrel Courier</div>
  <p class="abs copy">Copyrights @ 2018 All Rights Reserved</p>
</footer>

</body>
</html>
```